Brightpath Dentistry - Flyer - Modern & Eye catching campaign flyer

Need front & back side full page flyer designs for both 1) Grand opening 2) On-going campaign.

Attached the new dental office logo.
Attached our other dental clinic flyer designs for content.

Target Market(s)

Cosmetic dentistry

Industry/Entity Type

Health Care

Requirements
Must have
• decent, modern and eye catching marketing flyers.
Nice to have
• - Nice space
• - Highlight phone number
• - Highlight special features like convenient hours, call or text, for all ages, digital facility, etc
Should not have
• - Don't want to fill the flyer with too much wordings
• - Too many colors

```html
<!DOCTYPE html>
<html lang="en">
<head>
<meta charset="utf-8">
<title>Brightpath Dentistry – Grand Opening Flyer</title>
<link href="https://fonts.googleapis.com/css2?family=Hind:wght@400;500;600;700&family=Ubuntu:wght@400;500;700&display=swap" rel="stylesheet">
<style>
  :root{
    --stage:#999999;
    --blue:#1f6bbd;
    --blue-deep:#1a5fb4;
    --blue-light:#0aa0da;
    --panel:rgba(40,110,200,.85);
    --white:#ffffff;
    --ink:#111111;
    --text:#333333;
    --green:#163f1a;
    --tick:#3aa64a;
  }
  *{margin:0;padding:0;box-sizing:border-box}
  html,body{width:1200px;height:1200px;overflow:hidden}
  body{background:var(--stage);font-family:"Hind",sans-serif;position:relative}
  .flyer{position:absolute;top:227px;width:527px;height:744px;background:var(--white);overflow:hidden;box-shadow:6px 8px 14px rgba(0,0,0,.35)}
  .front{left:46px}
  .back{left:622px}
  .abs{position:absolute}

  /* front */
  .hero-photo{left:0;top:0;width:527px;height:350px;background:linear-gradient(110deg,#6f8fb8 0%,#c9a08e 45%,#e89aa8 70%,#8fae5a 100%)}
  .hero-panel{left:24px;top:0;width:251px;height:350px;background:var(--panel)}
  .brand{left:38px;top:48px;display:flex;align-items:center;gap:8px;color:var(--white);font-weight:600;font-size:20px;letter-spacing:.5px}
  .brand-dot{width:16px;height:16px;border-radius:50%;background:var(--white)}
  .headline-top{left:38px;top:116px;color:var(--white);font-size:27px;font-weight:500;letter-spacing:.3px}
  .headline-main{left:52px;top:150px;color:var(--white);font-size:43px;font-weight:700;letter-spacing:1px}
  .offers{left:38px;top:222px;list-style:none;color:var(--white);font-size:14.5px}
  .offers li{display:flex;align-items:center;gap:9px;height:32px}
  .offers b{font-size:19px;font-weight:700}
  .tick{width:12px;height:12px;flex:none}
  .services-title{left:0;top:350px;width:527px;height:38px;padding-left:38px;line-height:40px;color:var(--blue);font-weight:700;font-size:17px}
  .services-body{left:0;top:388px;width:527px;height:281px;background:linear-gradient(135deg,var(--blue-deep) 0%,#1e74c4 60%,var(--blue-light) 100%)}
  .svc{list-style:none;color:var(--white);font-size:14.5px;position:absolute;top:14px}
  .svc li{display:flex;align-items:center;gap:15px;height:31px}
  .svc-left{left:38px}
  .svc-right{left:353px}
  .svc-divider{position:absolute;left:316px;top:10px;height:150px;border-left:1px dashed rgba(255,255,255,.7)}
  .hours-pill{position:absolute;left:54px;top:184px;width:418px;height:35px;border-radius:18px;background:var(--white);color:var(--blue);font-size:17px;font-weight:500;text-align:center;line-height:37px}
  .note{position:absolute;left:0;width:527px;text-align:center;color:var(--white);font-size:14px}
  .front-footer{left:0;top:669px;width:527px;height:75px;display:flex;align-items:center}
  .phone{display:flex;align-items:center;gap:14px;padding-left:38px;width:306px;font-size:36px;font-weight:500;letter-spacing:1px;flex:none}
  .front-footer .phone{color:var(--ink)}
  .v-rule{width:1px;height:48px;background:currentColor;flex:none}
  .contacts{padding-left:16px;font-size:12px;color:var(--ink);line-height:29px;white-space:nowrap}
  .contacts div{display:flex;align-items:center;gap:9px}
  .contacts b{font-weight:700}

  /* back */
  .back-photo{left:0;top:0;width:527px;height:320px;background:linear-gradient(120deg,#d9d4cc 0%,#c8a88a 40%,#e8dccb 70%,#b9c2b4 100%)}
  .back-band{left:0;top:320px;width:527px;height:9px;background:var(--blue)}
  .badge{left:361px;top:217px;width:144px;height:144px;border-radius:50%;background:linear-gradient(160deg,#0aa0da,var(--blue-deep));color:var(--white);text-align:center;display:flex;flex-direction:column;justify-content:center;font-size:19px;line-height:29px;box-shadow:0 3px 8px rgba(0,0,0,.25)}
  .badge b{font-weight:700}
  .h2{left:38px;color:var(--green);font-family:"Ubuntu",sans-serif;font-size:22px;font-weight:400}
  .para{left:39px;width:450px;color:var(--text);font-size:10.6px;line-height:14px;text-align:justify}
  .doctor{left:0;width:420px;text-align:center;top:514px;font-size:14px;color:var(--green)}
  .sub{left:39px;top:548px;font-size:12.5px;font-weight:700;color:var(--ink);letter-spacing:.2px}
  .features{left:39px;top:572px;width:300px;list-style:none;font-size:12.5px;color:var(--ink);line-height:15px}
  .features li{display:flex;gap:12px;margin-bottom:4px}
  .features .tick{margin-top:2px}
  .map{left:351px;top:567px;width:149px;height:87px;background:linear-gradient(135deg,#e6e8eb,#d7dce2);border:2px solid var(--blue)}
  .back-footer{left:0;top:670px;width:527px;height:74px;background:linear-gradient(90deg,var(--blue-deep),var(--blue-light));display:flex;align-items:center;color:var(--white)}
  .back-footer .phone{color:var(--white)}
  .address{display:flex;align-items:center;gap:10px;padding-left:18px;font-size:11px;line-height:13px}
</style>
</head>
<body>

<section class="flyer front">
  <div class="abs hero-photo" role="img" aria-label="Photo of a smiling father carrying his daughter on his back outdoors"></div>
  <div class="abs hero-panel"></div>
  <div class="abs brand"><span class="brand-dot"></span>Brightpath Dentistry</div>
  <div class="abs headline-top">GRAND OPENING</div>
  <div class="abs headline-main">SPECIALS</div>
  <ul class="abs offers">
    <li><svg class="tick" viewBox="0 0 12 12"><circle cx="6" cy="6" r="5" fill="none" stroke="#fff" stroke-width="1.2"/><path d="M3.5 6l2 2 3.5-4" fill="none" stroke="#fff" stroke-width="1.3"/></svg>Free Kids Dental Screening</li>
    <li><svg class="tick" viewBox="0 0 12 12"><circle cx="6" cy="6" r="5" fill="none" stroke="#fff" stroke-width="1.2"/><path d="M3.5 6l2 2 3.5-4" fill="none" stroke="#fff" stroke-width="1.3"/></svg><span><b>$25</b> Adults Dental Screening</span></li>
    <li><svg class="tick" viewBox="0 0 12 12"><circle cx="6" cy="6" r="5" fill="none" stroke="#fff" stroke-width="1.2"/><path d="M3.5 6l2 2 3.5-4" fill="none" stroke="#fff" stroke-width="1.3"/></svg><span><b>15%</b> Off On Treatment Plan</span></li>
  </ul>

  <div class="abs services-title">OUR SERVICES</div>
  <div class="abs services-body">
    <ul class="svc svc-left">
      <li><svg class="tick" viewBox="0 0 12 12"><circle cx="6" cy="6" r="5" fill="none" stroke="#fff" stroke-width="1.2"/><path d="M3.5 6l2 2 3.5-4" fill="none" stroke="#fff" stroke-width="1.3"/></svg>ROOT CANAL THERAPY</li>
      <li><svg class="tick" viewBox="0 0 12 12"><circle cx="6" cy="6" r="5" fill="none" stroke="#fff" stroke-width="1.2"/><path d="M3.5 6l2 2 3.5-4" fill="none" stroke="#fff" stroke-width="1.3"/></svg>GLOW TEETH WHITENING</li>
      <li><svg class="tick" viewBox="0 0 12 12"><circle cx="6" cy="6" r="5" fill="none" stroke="#fff" stroke-width="1.2"/><path d="M3.5 6l2 2 3.5-4" fill="none" stroke="#fff" stroke-width="1.3"/></svg>EXTRACTIONS</li>
      <li><svg class="tick" viewBox="0 0 12 12"><circle cx="6" cy="6" r="5" fill="none" stroke="#fff" stroke-width="1.2"/><path d="M3.5 6l2 2 3.5-4" fill="none" stroke="#fff" stroke-width="1.3"/></svg>CLEARLINE (INVISIBLE BRACES)</li>
      <li><svg class="tick" viewBox="0 0 12 12"><circle cx="6" cy="6" r="5" fill="none" stroke="#fff" stroke-width="1.2"/><path d="M3.5 6l2 2 3.5-4" fill="none" stroke="#fff" stroke-width="1.3"/></svg>CROWN AND BRIDGE</li>
    </ul>
    <div class="svc-divider"></div>
    <ul class="svc svc-right">
      <li><svg class="tick" viewBox="0 0 12 12"><circle cx="6" cy="6" r="5" fill="none" stroke="#fff" stroke-width="1.2"/><path d="M3.5 6l2 2 3.5-4" fill="none" stroke="#fff" stroke-width="1.3"/></svg>IMPLANTS</li>
      <li><svg class="tick" viewBox="0 0 12 12"><circle cx="6" cy="6" r="5" fill="none" stroke="#fff" stroke-width="1.2"/><path d="M3.5 6l2 2 3.5-4" fill="none" stroke="#fff" stroke-width="1.3"/></svg>VENEERS</li>
      <li><svg class="tick" viewBox="0 0 12 12"><circle cx="6" cy="6" r="5" fill="none" stroke="#fff" stroke-width="1.2"/><path d="M3.5 6l2 2 3.5-4" fill="none" stroke="#fff" stroke-width="1.3"/></svg>DENTURES</li>
      <li><svg class="tick" viewBox="0 0 12 12"><circle cx="6" cy="6" r="5" fill="none" stroke="#fff" stroke-width="1.2"/><path d="M3.5 6l2 2 3.5-4" fill="none" stroke="#fff" stroke-width="1.3"/></svg>NIGHT GUARDS</li>
    </ul>
    <div class="hours-pill">CONVENIENT EVENING &amp; SATURDAY HOURS</div>
    <p class="note" style="top:228px">NEW PATIENTS ONLY. OFFER EXPIRES IN <b>30</b> DAYS.</p>
    <p class="note" style="top:251px;font-weight:700">NEW PATIENTS ARE WELCOME!</p>
  </div>

  <div class="abs front-footer">
    <div class="phone">
      <svg width="30" height="30" viewBox="0 0 30 30"><circle cx="15" cy="15" r="13" fill="none" stroke="#111" stroke-width="2"/><path d="M10 8c-1 1-1.5 3 0 6s4 6 7 7.5c2 1 3.5.5 4.5-.5l-2.5-3-2 1c-1.5-1-3-2.5-4-4l1-2z" fill="#111"/></svg>
      6105550142
    </div>
    <div class="v-rule" style="color:#111"></div>
    <div class="contacts">
      <div><svg width="14" height="14" viewBox="0 0 14 14"><circle cx="7" cy="7" r="6" fill="none" stroke="#111"/><ellipse cx="7" cy="7" rx="2.5" ry="6" fill="none" stroke="#111"/><path d="M1 7h12" stroke="#111"/></svg><span>www.<b>brightpathdental</b>.com</span></div>
      <div><svg width="14" height="12" viewBox="0 0 14 12"><rect x="1" y="2" width="12" height="8" fill="#111"/><path d="M1 2l6 5 6-5" fill="none" stroke="#fff"/></svg><span>info@<b>brightpathdental</b>.com</span></div>
    </div>
  </div>
</section>

<section class="flyer back">
  <div class="abs back-photo" role="img" aria-label="Photo of two women chatting and smiling over coffee at a café table"></div>
  <div class="abs back-band"></div>
  <div class="abs badge"><span>ALL</span><b>INSURANCES</b><span>ACCEPTED</span></div>

  <h2 class="abs h2" style="top:348px">We accept most insurance forms !</h2>
  <p class="abs para" style="top:382px">For your convenience, we accept most insurance plans and will be happy to help you understand the coverage that you have. We will do our best to see that you receive your maximum insurance benefits for all covered services, however, please note that dental insurance is intended to cover some, but not all, of the cost of your care.</p>
  <h2 class="abs h2" style="top:450px">looking for dentist close to home?</h2>
  <p class="abs para" style="top:484px;text-align:left">come and see us for professional services and staff are experts in the will help you achieve your perfect smile.</p>
  <p class="abs doctor">( Dr. Maya Calder, D.D.S. )</p>

  <p class="abs sub">FAMILY &amp; COSMETIC DENTISTRY</p>
  <ul class="abs features">
    <li><svg class="tick" viewBox="0 0 12 12"><circle cx="6" cy="6" r="5" fill="none" stroke="#3aa64a" stroke-width="1.2"/><path d="M3.5 6l2 2 3.5-4" fill="none" stroke="#3aa64a" stroke-width="1.3"/></svg>state of the art equipment and paperless facility.</li>
    <li><svg class="tick" viewBox="0 0 12 12"><circle cx="6" cy="6" r="5" fill="none" stroke="#3aa64a" stroke-width="1.2"/><path d="M3.5 6l2 2 3.5-4" fill="none" stroke="#3aa64a" stroke-width="1.3"/></svg>filled with entertalment devices for patient.</li>
    <li><svg class="tick" viewBox="0 0 12 12"><circle cx="6" cy="6" r="5" fill="none" stroke="#3aa64a" stroke-width="1.2"/><path d="M3.5 6l2 2 3.5-4" fill="none" stroke="#3aa64a" stroke-width="1.3"/></svg>same day apponment for dental emergence</li>
    <li><svg class="tick" viewBox="0 0 12 12"><circle cx="6" cy="6" r="5" fill="none" stroke="#3aa64a" stroke-width="1.2"/><path d="M3.5 6l2 2 3.5-4" fill="none" stroke="#3aa64a" stroke-width="1.3"/></svg>helping community with routine free kids dental screening.</li>
  </ul>
  <div class="abs map" role="img" aria-label="Street map showing the clinic location"></div>

  <div class="abs back-footer">
    <div class="phone">
      <svg width="30" height="30" viewBox="0 0 30 30"><circle cx="15" cy="15" r="13" fill="none" stroke="#fff" stroke-width="2"/><path d="M10 8c-1 1-1.5 3 0 6s4 6 7 7.5c2 1 3.5.5 4.5-.5l-2.5-3-2 1c-1.5-1-3-2.5-4-4l1-2z" fill="#fff"/></svg>
      6105550142
    </div>
    <div class="v-rule"></div>
    <div class="address">
      <svg width="12" height="16" viewBox="0 0 12 16"><path d="M6 0a6 6 0 0 0-6 6c0 4.5 6 10 6 10s6-5.5 6-10a6 6 0 0 0-6-6z" fill="#fff"/><circle cx="6" cy="6" r="2.2" fill="#1a5fb4"/></svg>
      <span>412 Linden Pike, Maple<br>Hill PA 19000</span>
    </div>
  </div>
</section>

</body>
</html>
```